Velvet Afterhours Poster Design

Need poster design made up in next few days, can guarantee payment to winner. Poster must contain the following but feel free to word it better:
Velvet Afterhours
Presented by quendor Sounds
Select resident djs
Drink specials all night
Open from 8pm to 12pm
Find us on Fanspace
At Marlow Suites every Saturday
These will be on posters and fliers
Of a3 and roughly a5 size.
Our target audience is people 18-25
We want the posters to be exciting and professional. We would like a blue or purple with black color scheme but there is plenty of room for creative license so have a play around with what you think looks good. We currently don't have a logo but if your including one we would like to see it as c6 as in carbon as an element. Our first drink special is cocktails in jars but is not essential to include, can provide proper copy of the picture if you want to include it in your design. Please contact us if you need more information. we will be quick to pick a winner so payment will be provided fast!!!
Thank you all in advance for your submissions!!

```html
<!DOCTYPE html>
<html lang="en">
<head>
<meta charset="utf-8">
<title>Velvet Afterhours – Poster</title>
<link rel="stylesheet" href="https://fonts.googleapis.com/css2?family=Orbitron:wght@900&family=Michroma&family=Lato:wght@400&family=Kaushan+Script&display=swap">
<style>
  :root {
    --ink: #0d0d10;
    --charcoal: #2a2a2e;
    --violet: #c21cff;
    --magenta: #e02cff;
    --cyan: #2ee6ff;
    --ice: #f3f4ff;
    --lavender: #e4d2ff;
    --text-glow: rgba(120, 30, 200, 0.85);
  }
  * { margin: 0; padding: 0; box-sizing: border-box; }
  html, body {
    width: 848px; height: 1200px; overflow: hidden;
    background: var(--ink);
  }
  .poster {
    position: relative;
    width: 848px; height: 1200px; overflow: hidden;
    background: radial-gradient(ellipse at 50% 100%, #4a4a4f 0%, var(--charcoal) 35%, var(--ink) 80%);
  }
  .backdrop { position: absolute; inset: 0; width: 848px; height: 1200px; }
  .copy {
    position: absolute; left: 0; width: 848px;
    text-align: center; color: var(--ice);
    white-space: nowrap;
  }
  .title-main {
    top: 170px;
    font-family: "Orbitron", sans-serif; font-weight: 900;
    font-size: 130px; letter-spacing: 8px; line-height: 1;
    color: #3b1760;
    -webkit-text-stroke: 8px var(--ice);
    paint-order: stroke fill;
    text-shadow: 0 0 18px rgba(255,255,255,0.35);
  }
  .title-script {
    top: 268px;
    font-family: "Kaushan Script", cursive;
    font-size: 142px; line-height: 1.3;
    color: var(--ice);
    text-shadow: 0 4px 14px rgba(40, 0, 70, 0.6);
    transform: skewX(-6deg);
  }
  .presenter {
    top: 552px;
    font-family: "Lato", sans-serif; font-size: 22px;
    letter-spacing: 0.5px; color: var(--lavender);
    text-shadow: 0 0 6px var(--text-glow);
  }
  .highlights {
    top: 594px;
    font-family: "Michroma", sans-serif;
    font-size: 41px; line-height: 50px;
    color: var(--lavender);
    text-shadow: 2px 3px 6px var(--text-glow), 0 0 2px #fff;
  }
  .hours {
    top: 698px;
    font-family: "Michroma", sans-serif;
    font-size: 56px; line-height: 70px;
    color: var(--ice);
    text-shadow: 2px 3px 8px var(--text-glow);
  }
  .details {
    top: 1062px;
    font-family: "Michroma", sans-serif;
    font-size: 23px; line-height: 33px;
    color: var(--ice);
    text-shadow: 1px 2px 4px rgba(0,0,0,0.7);
  }
</style>
</head>
<body>
<main class="poster">
  <svg class="backdrop" viewBox="0 0 848 1200" aria-hidden="true">
    <defs>
      <linearGradient id="stripe-violet" x1="0" y1="0" x2="0" y2="1">
        <stop offset="0" stop-color="var(--magenta)"/>
        <stop offset="1" stop-color="#8a20d8"/>
      </linearGradient>
      <linearGradient id="veil" x1="0" y1="0" x2="0" y2="1">
        <stop offset="0" stop-color="#ffffff" stop-opacity="0.18"/>
        <stop offset="1" stop-color="#ffffff" stop-opacity="0.08"/>
      </linearGradient>
      <radialGradient id="pool-cyan">
        <stop offset="0" stop-color="var(--cyan)" stop-opacity="0.55"/>
        <stop offset="1" stop-color="var(--cyan)" stop-opacity="0"/>
      </radialGradient>
      <radialGradient id="pool-violet">
        <stop offset="0" stop-color="var(--violet)" stop-opacity="0.5"/>
        <stop offset="1" stop-color="var(--violet)" stop-opacity="0"/>
      </radialGradient>
    </defs>

    <!-- violet stripes, upper half -->
    <g class="stripes-violet" fill="url(#stripe-violet)">
      <rect x="64" y="0" width="38" height="532" opacity="0.85"/>
      <rect x="130" y="0" width="60" height="532" opacity="0.7"/>
      <rect x="232" y="0" width="44" height="532" opacity="0.9"/>
      <rect x="320" y="0" width="70" height="532" opacity="0.6"/>
      <rect x="408" y="0" width="56" height="532" opacity="0.95"/>
      <rect x="500" y="0" width="46" height="532" opacity="0.7"/>
      <rect x="585" y="0" width="70" height="532" opacity="0.9"/>
      <rect x="690" y="0" width="48" height="532" opacity="0.75"/>
      <rect x="770" y="0" width="40" height="532" opacity="0.6"/>
    </g>

    <!-- cyan band, lower half -->
    <g class="stripes-cyan" fill="var(--cyan)">
      <rect x="0" y="532" width="60" height="260" opacity="0.75"/>
      <rect x="96" y="532" width="80" height="340" opacity="0.85"/>
      <rect x="250" y="532" width="50" height="320" opacity="0.55"/>
      <rect x="540" y="532" width="60" height="300" opacity="0.6"/>
      <rect x="660" y="532" width="100" height="360" opacity="0.8"/>
      <rect x="800" y="532" width="48" height="300" opacity="0.75"/>
    </g>
    <rect class="stripe-violet-low" x="300" y="532" width="40" height="430" fill="var(--violet)" opacity="0.75"/>
    <rect class="stripe-violet-low" x="470" y="532" width="36" height="400" fill="var(--violet)" opacity="0.6"/>

    <!-- diamonds -->
    <polygon class="diamond-outer" points="435,53 787,545 435,1036 85,545" fill="var(--cyan)" opacity="0.32"/>
    <polygon class="diamond-inner" points="435,190 690,545 435,900 180,545" fill="#141418" opacity="0.55"/>
    <polygon class="diamond-edge" points="435,53 787,545 435,1036 85,545" fill="none" stroke="var(--cyan)" stroke-width="3" opacity="0.7"/>
    <polygon class="diamond-side" points="0,260 200,545 0,830" fill="var(--cyan)" opacity="0.25"/>
    <polygon class="diamond-side" points="848,260 650,545 848,830" fill="var(--cyan)" opacity="0.25"/>

    <!-- nested outline diamonds -->
    <g class="diamond-rings" fill="none" stroke-width="1.5">
      <polygon points="435,120 740,545 435,970 132,545" stroke="var(--magenta)" opacity="0.45"/>
      <polygon points="435,250 648,545 435,840 222,545" stroke="var(--cyan)" opacity="0.5"/>
    </g>

    <!-- translucent title veil -->
    <rect class="title-veil" x="0" y="165" width="848" height="367" fill="url(#veil)"/>

    <!-- soft light pools -->
    <g class="light-pools">
      <circle cx="435" cy="545" r="260" fill="url(#pool-violet)"/>
      <circle cx="435" cy="1036" r="180" fill="url(#pool-cyan)"/>
      <circle cx="85" cy="545" r="120" fill="url(#pool-cyan)"/>
      <circle cx="787" cy="545" r="120" fill="url(#pool-cyan)"/>
    </g>
  </svg>

  <h1 class="copy title-main">VELVET</h1>
  <p class="copy title-script">Afterhours</p>
  <p class="copy presenter">PRESENTED BY QUENDOR SOUNDS</p>
  <p class="copy highlights">SELECT RESIDENT DJS<br>DRINK SPECIALS ALL NIGHT</p>
  <p class="copy hours">OPEN FROM<br>8PM TO 12PM</p>
  <p class="copy details">Find us on Fanspace<br>At Marlow Suites every Saturday</p>
</main>
</body>
</html>
```